Box for a Bold Bathroom - stylish minimalist package for a modern upscale brand

We need an adaptable package design using a color label on a brown box, or just a brown box with 2 or 3 color printing. The best design would be one that is adaptable for either use.

Our first products launching under this brand will be a series of medicine cabinets and mirrors, and our cartons can vary in size from 500x100x600 mm to 1200x300x1000 mm

About us: we produce a variety of bathroom fixtures including medicine cabinets, mirrors, vanities, etc. You've likely seen our products - we do manufacturing for Brantley, Marnova, Tusk Harbor, Penn & Waite, and others.

A version of our logo is attached for reference; we use it in a variety of color mixes depending on application. Vector available if needed or can be used FPO and our team will replace.

These are our colors, please take note and ignore the 'color' field:

Light Blue: C:66%/M:6%/Y:22%/K:0%; H:189° S:65% B:78%
Light Grey: C:35%/M:26%/Y:24%/K:0%; H:213° S:5% B:70%
Dark Blue: C:90%/M:50%/Y:44%/K:20%; H:189° S:82% B:43%
Dark Grey: C:70%/M:60%/Y:54%/K:38%; H:213° S:11% B:30%

Project Deadline Extended
Reason: Some revisions still outstanding before we can make selection, and some submissions we have agreed to wait for. Please submit all work ASAP so our team can provide feedback to you. Thanks!

Target Market(s)

DIY'ers; home renovators

Industry/Entity Type

Home Improvement

Font styles to use
Sans Serif

Requirements
Must have
• 1. Brand logo w/ logotype
• 2. Brand name without logo (can be on shipping mark side)
• 3. Multi-lingual En/Fr/Es (you do not need to include multi-lingual content but must allow space for our own translations if you do not)
• 4. Shipping/Handling Glyphs on 5 sides (all but bottom)
• i.e. fragile, this way up, team lift or mech lift, clamp or no clamp, max-stack
• 5. Two sides should include a marked 4" x 4" area for affixing labels (e.g. UPC, SSCC, etc.) ideally with a dotted line or corner marks or similar.
• 6. Shipping mark details or space for them (should be on the smallest side, only needed on one but can be on both) [see example file of shipping mark informations]
Nice to have
• Design that can be used either with color label on brown box, or brown box only.
• If designing for color label; please see the sample images included. Lifestyle should be prominent, the inside photo being smaller to help show interior features. These photos are obviously not useful for brown-box design.

```html
<!DOCTYPE html>
<html lang="en">
<head>
<meta charset="utf-8">
<title>Northglass — Shipping Carton Dieline</title>
<link href="https://fonts.googleapis.com/css2?family=Jost:ital,wght@0,300;0,400;0,600;1,600&family=Roboto+Condensed:wght@400&display=swap" rel="stylesheet">
<style>
  :root {
    --page-bg: #e9eaeb;
    --kraft: #b69274;
    --kraft-edge: #8e6f56;
    --teal-dark: #2c6573;
    --blue-light: #44b8c9;
    --grey-dark: #42484f;
    --grey-light: #a9adb3;
    --white: #ffffff;
  }
  html, body {
    margin: 0;
    padding: 0;
    width: 1200px;
    height: 1200px;
    overflow: hidden;
    background: var(--page-bg);
  }
  .dieline { display: block; width: 1200px; height: 1200px; }
  .panel { fill: var(--kraft); stroke: var(--kraft-edge); stroke-width: 0.8; }
  .fold { stroke: var(--kraft-edge); stroke-width: 0.8; fill: none; }
  .rule-teal { stroke: var(--teal-dark); stroke-width: 3; }
  .swoosh { fill: none; stroke: var(--teal-dark); stroke-width: 16; }
  .white-area { fill: var(--white); }
  .tagline { font-family: "Jost", sans-serif; font-weight: 600; font-style: italic; font-size: 19px; fill: var(--grey-dark); letter-spacing: 0.5px; }
  .brand { font-family: "Jost", sans-serif; font-weight: 400; fill: var(--grey-dark); letter-spacing: 1.6px; }
  .brand-mark { fill: var(--blue-light); }
  .ship-block { fill: var(--teal-dark); }
  .ship-text { font-family: "Roboto Condensed", sans-serif; font-size: 5.6px; fill: var(--blue-light); }
  .glyph-frame { fill: none; stroke: var(--grey-dark); stroke-width: 1.2; }
  .glyph-line { fill: none; stroke: var(--grey-dark); stroke-width: 1.6; }
  .glyph-fill { fill: var(--grey-dark); }
  .glyph-num { font-family: "Jost", sans-serif; font-weight: 600; font-size: 13px; fill: var(--grey-dark); }
  .label-zone { fill: var(--white); stroke: var(--grey-dark); stroke-width: 1.2; stroke-dasharray: 2 2; }
  .blank-sheet { fill: var(--white); }
</style>
</head>
<body>
<svg class="dieline" viewBox="0 0 1500 1500" xmlns="http://www.w3.org/2000/svg">
  <defs>
    <linearGradient id="lifestyle-tone" x1="0" y1="0" x2="1" y2="1">
      <stop offset="0" stop-color="#c9d9e0"/>
      <stop offset="0.45" stop-color="#a7bfca"/>
      <stop offset="0.8" stop-color="#e6eef1"/>
      <stop offset="1" stop-color="#ffffff"/>
    </linearGradient>
    <linearGradient id="lifestyle-tone-flip" x1="1" y1="1" x2="0" y2="0">
      <stop offset="0" stop-color="#c9d9e0"/>
      <stop offset="0.45" stop-color="#a7bfca"/>
      <stop offset="0.8" stop-color="#e6eef1"/>
      <stop offset="1" stop-color="#ffffff"/>
    </linearGradient>
    <clipPath id="front-white">
      <path d="M385,325 L1196,325 L1196,678 C700,660 460,460 385,325 Z"/>
    </clipPath>
    <clipPath id="back-white">
      <path d="M328,1020 C700,1060 960,1200 1100,1380 L328,1380 Z"/>
    </clipPath>

    <symbol id="handling-glyphs" viewBox="0 0 176 30">
      <rect class="glyph-frame" x="1" y="1" width="30" height="28"/>
      <path class="glyph-line" d="M10,24 V8 M6,12 L10,7 L14,12 M21,24 V8 M17,12 L21,7 L25,12 M6,25 H26"/>
      <rect class="glyph-frame" x="36" y="1" width="30" height="28"/>
      <path class="glyph-line" d="M44,12 L51,8 L58,12 L51,16 Z M44,12 V20 L51,24 L58,20 V12 M40,20 L46,26 M62,20 L56,26"/>
      <rect class="glyph-frame" x="71" y="1" width="30" height="28"/>
      <path class="glyph-fill" d="M79,6 H93 L91,15 Q86,19 81,15 Z"/>
      <path class="glyph-line" d="M86,17 V24 M81,25 H91"/>
      <rect class="glyph-frame" x="106" y="1" width="30" height="28"/>
      <path class="glyph-line" d="M113,9 H129 V22 H113 Z M109,5 L133,26 M133,5 L109,26"/>
      <rect class="glyph-frame" x="141" y="1" width="34" height="28"/>
      <text class="glyph-num" x="149" y="21">10</text>
      <path class="glyph-line" d="M146,25 H170"/>
    </symbol>
  </defs>

  <!-- top closure -->
  <path class="panel" d="M506,122 L508,100 Q512,85 530,85 L970,85 Q988,85 992,100 L994,122 Z"/>
  <rect class="panel" x="506" y="122" width="488" height="201"/>
  <path class="panel" d="M312,127 L506,122 L506,323 L312,323 Z"/>
  <path class="panel" d="M994,122 L1188,127 L1188,323 L994,323 Z"/>
  <rect x="674" y="114" width="152" height="6" class="white-area"/>
  <text class="tagline" x="757" y="222" text-anchor="middle" transform="rotate(180 757 215)">STYLISH BATHROOM fixtures</text>

  <!-- body band -->
  <path class="panel" d="M118,323 L118,430 L108,440 L108,635 L118,645 L118,752 L303,752 L303,323 Z"/>
  <rect class="panel" x="303" y="323" width="203" height="429"/>
  <rect class="panel" x="506" y="323" width="488" height="429"/>
  <rect class="panel" x="994" y="323" width="202" height="429"/>
  <path class="panel" d="M1196,323 L1382,323 L1382,430 L1392,440 L1392,635 L1382,645 L1382,752 L1196,752 Z"/>

  <path class="white-area" d="M385,325 L1196,325 L1196,678 C700,660 460,460 385,325 Z"/>
  <g clip-path="url(#front-white)">
    <rect x="506" y="325" width="560" height="360" fill="url(#lifestyle-tone)" role="img" aria-label="Lifestyle photo of a modern bathroom vanity with a dark vessel sink, chrome faucet and wall cabinet"/>
  </g>
  <path class="swoosh" d="M390,330 C465,468 700,668 1196,686"/>

  <line class="rule-teal" x1="118" y1="325" x2="1382" y2="325"/>
  <line class="rule-teal" x1="118" y1="750" x2="1382" y2="750"/>

  <!-- shipping marks -->
  <g class="shipping-marks">
    <rect class="ship-block" x="364" y="393" width="154" height="87"/>
    <text class="ship-text" x="375" y="404">LOT#: 0000000</text>
    <text class="ship-text" x="375" y="412">ITEM #: XXXX00</text>
    <text class="ship-text" x="375" y="420">DIM: 000 X 00 X 00 CM</text>
    <text class="ship-text" x="385" y="428">00" X 00" X 00"</text>
    <text class="ship-text" x="375" y="436">NW / PK: 00 KG</text>
    <text class="ship-text" x="375" y="444">GW / PK: 00 KG</text>
    <text class="ship-text" x="375" y="452">CUBE: 0.00 M3</text>
    <text class="ship-text" x="375" y="460">QTY: 1</text>
    <text class="ship-text" x="375" y="468">CASE</text>

    <rect class="ship-block" x="364" y="487" width="154" height="86"/>
    <text class="ship-text" x="375" y="498">LOT#: 0000000</text>
    <text class="ship-text" x="375" y="506">ITEM #: XXXX00</text>
    <text class="ship-text" x="375" y="514">DIM: 000 X 00 X 00 CM</text>
    <text class="ship-text" x="385" y="522">00" X 00" X 00"</text>
    <text class="ship-text" x="375" y="530">NW / PK: 00 KG</text>
    <text class="ship-text" x="375" y="538">GW / PK: 00 KG</text>
    <text class="ship-text" x="375" y="546">CUBE: 0.00 M3</text>
    <text class="ship-text" x="375" y="554">QTY: 1</text>
    <text class="ship-text" x="375" y="562">CASE</text>

    <rect class="ship-block" x="364" y="582" width="154" height="85"/>
    <text class="ship-text" x="375" y="593">LOT#: 0000000</text>
    <text class="ship-text" x="375" y="601">ITEM #: XXXX00</text>
    <text class="ship-text" x="375" y="609">DIM: 000 X 00 X 00 CM</text>
    <text class="ship-text" x="385" y="617">00" X 00" X 00"</text>
    <text class="ship-text" x="375" y="625">NW / PK: 00 KG</text>
    <text class="ship-text" x="375" y="633">GW / PK: 00 KG</text>
    <text class="ship-text" x="375" y="641">CUBE: 0.00 M3</text>
    <text class="ship-text" x="375" y="649">QTY: 1</text>
    <text class="ship-text" x="375" y="657">CASE</text>
  </g>

  <!-- front brand -->
  <circle class="brand-mark" cx="596" cy="382" r="8"/>
  <text class="brand" x="543" y="412" font-size="11">NORTHGLASS</text>

  <!-- side brand, vertical -->
  <circle class="brand-mark" cx="1155" cy="368" r="8"/>
  <text class="brand" x="1148" y="392" font-size="14" transform="rotate(90 1148 392)">NORTHGLASS</text>

  <!-- handling glyphs -->
  <use href="#handling-glyphs" x="340" y="708" width="130" height="23"/>
  <use href="#handling-glyphs" x="530" y="701" width="176" height="30"/>
  <use href="#handling-glyphs" x="1030" y="708" width="130" height="23"/>

  <rect class="label-zone" x="928" y="688" width="45" height="45"/>

  <!-- lower flaps -->
  <path class="panel" d="M312,757 L506,752 L506,952 L312,952 Z"/>
  <rect class="panel" x="506" y="752" width="488" height="200"/>
  <path class="panel" d="M994,752 L1188,757 L1188,952 L994,952 Z"/>
  <text class="brand" x="750" y="860" font-size="18" text-anchor="middle" transform="rotate(180 750 853)">NORTHGLASS</text>

  <!-- back panel -->
  <path class="panel" d="M506,952 L506,1380 L370,1350 Q328,1340 328,1300 L328,1020 Q328,990 360,982 Z"/>
  <rect class="panel" x="506" y="952" width="488" height="428"/>
  <path class="panel" d="M994,952 L1140,985 Q1172,992 1172,1025 L1172,1320 Q1172,1348 1140,1355 L994,1380 Z"/>
  <path class="panel" d="M683,1380 L817,1380 L817,1405 Q817,1415 807,1415 L693,1415 Q683,1415 683,1405 Z"/>

  <path class="white-area" d="M328,1020 C700,1060 960,1200 1100,1380 L370,1380 Q328,1370 328,1330 Z"/>
  <g clip-path="url(#back-white)">
    <rect x="440" y="1020" width="560" height="395" fill="url(#lifestyle-tone-flip)" role="img" aria-label="Lifestyle photo of a modern bathroom vanity with a dark vessel sink and chrome fittings, shown inverted"/>
  </g>
  <path class="swoosh" d="M328,1020 C700,1048 972,1190 1104,1380"/>
  <line class="rule-teal" x1="506" y1="953" x2="994" y2="953"/>

  <circle class="brand-mark" cx="903" cy="1325" r="8"/>
  <text class="brand" x="902" y="1301" font-size="10" text-anchor="middle" transform="rotate(180 902 1297)">NORTHGLASS</text>

  <use href="#handling-glyphs" x="797" y="982" width="174" height="30" transform="rotate(180 884 997)"/>
  <rect class="label-zone" x="526" y="970" width="45" height="46"/>

  <rect class="blank-sheet" x="1193" y="972" width="87" height="164"/>
</svg>
</body>
</html>
```